依頼詳細
【サイトの最大の要望は?】
○生命を扱う業種なので、信頼性と安心感があるサイトにしたい

【ターゲット】
20代~60代 男性・女性

フレンチブルドックに興味がある方がターゲットとなりますので、基本的には万人受けするようなデザインが希望です。

<強化したい項目>
・新規顧客増加
・サービス内容の訴求など会社パンフレット的な役割

◆サイトマップ
サイトマップ添付します

◆参考キーワード
・シンプル
・見やすい
・安心感
・信頼性
・親しみやすさ

◆参考にしたいサイト
https://kobatora-mock.jp/

◆素材について
写真素材につきましては、撮影イメージをダミーで制作していただけると助かります。テキストに関してもダミーテキストでも結構です。

※タスクリーフの規約にもありますが、通常業務に支障が出る為
直接電話等のお問い合わせをお控え頂けますよう、ご協力の程お願い致します。
ご不明点等ありましたら、内メッセージで頂戴できますと幸いです。
ページ数
2ページ
希望イメージ
シンプル 複雑
単色 カラフル
暗い 明るい
日常 高級
遊び心 厳粛
未来的 伝統的
女性的 男性的
希望する色
青系、水色系、緑系
納品ファイル
• 高解像度JPG (.jpg)
• イラストレーター形式 (.ai)
• フォトショップ形式 (.psd)
依頼公開後の追記内容
■ 選んだ理由

皆さま素敵なご提案を頂きましたが、他にはないイメージのご提案と、画像やフォントのご提案まで頂き、構築フェーズの制作環境がスムーズに行える、とてもありがたいご提案でした。

■ 提案者全員のお礼・コメント

皆さま素敵なデザインをお寄せ頂き、ありがとうございます。
今後も、案件が複数ございますので、是非宜しくお願い致します。
この度はありがとうございました。

```html
<!DOCTYPE html>
<html lang="ja">
<head>
<meta charset="utf-8">
<title>PUPLEAF フレンチブルドッグ専門ブリーダー</title>
<link href="https://fonts.googleapis.com/css2?family=Noto+Sans+JP:wght@400;500;700&family=Montserrat:wght@500;700&family=Playfair+Display:ital@0;1&display=swap" rel="stylesheet">
<style>
:root{
  --blue:#4a9fd8;
  --blue-soft:#dcecf8;
  --ink:#3a3a3a;
  --muted:#8a8a8a;
  --band:#f1f0ed;
  --line:#e2e2e2;
  --white:#ffffff;
  --navy:#2c3440;
}
*{margin:0;padding:0;box-sizing:border-box}
html,body{width:1200px;height:3720px;overflow:hidden}
body{font-family:"Noto Sans JP",sans-serif;color:var(--ink);background:var(--white);font-size:13px;line-height:1.8}
a{color:inherit;text-decoration:none}
.en{font-family:"Montserrat",sans-serif}
.ph{display:block}

/* hero */
.hero{position:relative;height:470px;background:linear-gradient(180deg,#a9cfe9 0%,#d7e8f2 30%,#8fb7c9 38%,#e9e0d0 46%,#d8c4a6 100%)}
.hero-copy{position:absolute;right:48px;top:34px;text-align:right;color:var(--navy)}
.hero-copy .lead{font-family:"Playfair Display",serif;font-size:22px;letter-spacing:.04em}
.hero-copy .sub{font-size:12px;letter-spacing:.12em}

/* header */
.site-header{position:relative;height:200px;padding:28px 70px 0 90px}
.brand{position:absolute;left:90px;top:-28px;width:120px;height:150px;display:flex;flex-direction:column;align-items:center;justify-content:flex-end;gap:8px}
.brand .mark{width:84px;height:84px;border-radius:50%;background:var(--blue)}
.brand .name{font-family:"Montserrat",sans-serif;font-weight:700;font-size:17px;letter-spacing:.08em;color:var(--navy)}
.header-info{margin-left:200px;display:flex;gap:24px;font-size:11px;color:var(--blue);align-items:center}
.nav{margin-left:250px;margin-top:22px;display:flex;align-items:center}
.nav a{color:var(--ink);text-align:center;width:112px;border-left:1px solid var(--line);font-size:13px;font-weight:500;line-height:1.5}
.nav a:last-of-type{border-right:1px solid var(--line)}
.nav a span{display:block;font-family:"Montserrat",sans-serif;font-size:9px;color:var(--blue);letter-spacing:.1em}
.search{margin-left:30px}

/* section titles */
.sec-title{text-align:center}
.sec-title .dot{width:30px;height:30px;border-radius:50%;border:2px solid var(--blue);margin:0 auto 6px}
.sec-title h2{font-size:20px;font-weight:700;letter-spacing:.1em}
.sec-title p{font-family:"Montserrat",sans-serif;font-size:9px;color:var(--blue);letter-spacing:.15em}

/* puppies */
.puppies{position:relative;padding:30px 0 60px;background:linear-gradient(180deg,var(--white) 0,var(--white) 140px,var(--band) 140px)}
.more{position:absolute;right:120px;top:118px;font-family:"Montserrat",sans-serif;font-size:11px;color:var(--ink)}
.puppy-grid{width:1000px;margin:36px auto 0;display:grid;grid-template-columns:repeat(5,1fr);gap:28px 14px}
.puppy .ph{height:138px;border-radius:2px}
.puppy .meta{font-size:11px;margin-top:6px;line-height:1.5}
.puppy .price{font-size:11px;color:var(--blue);font-family:"Montserrat",sans-serif}

/* news */
.news{position:relative;padding:70px 0 70px}
.news .feed{position:absolute;right:120px;top:150px;font-family:"Montserrat",sans-serif;font-size:11px}
.insta{width:1000px;margin:30px auto 0;display:grid;grid-template-columns:repeat(6,1fr);gap:6px}
.insta .ph{height:164px}

/* about */
.about{position:relative;height:960px;margin-top:30px}
.about-photo{position:absolute;left:70px;right:0;top:0;height:440px;background:linear-gradient(120deg,#6f9a5a 0%,#9dbf80 40%,#e5d9cf 60%,#d88aa3 100%)}
.about-card{position:absolute;left:70px;top:370px;width:600px;background:var(--white);padding:40px 70px 40px 80px}
.about-card h3{font-size:24px;font-weight:700;line-height:1.6;letter-spacing:.05em}
.about-card .tag{font-family:"Montserrat",sans-serif;font-size:10px;color:var(--blue);margin:10px 0 28px;letter-spacing:.1em}
.about-card p{font-size:13px;line-height:2.2;margin-bottom:22px}
.shop{position:absolute;left:820px;top:520px;width:320px}
.shop .ph{height:180px;background:linear-gradient(135deg,#e8ddd0,#b99c7e 70%,#8f7460)}
.shop .name{display:flex;align-items:center;gap:8px;justify-content:flex-end;margin-top:14px;font-family:"Montserrat",sans-serif;font-weight:700;font-size:17px;letter-spacing:.08em;color:var(--navy)}
.shop .name i{width:18px;height:18px;border-radius:50%;background:var(--blue)}
.shop .addr{font-size:11px;line-height:1.8;margin-top:8px;padding-left:40px}
.shop .link{text-align:right;font-family:"Montserrat",sans-serif;font-size:11px;margin-top:6px}

/* services */
.services{display:flex;justify-content:center;gap:40px;padding:20px 0 60px}
.service{position:relative;width:440px;height:250px;border-radius:14px;overflow:hidden;display:flex;flex-direction:column;align-items:center;justify-content:center;color:var(--white)}
.service .ph{position:absolute;inset:0}
.service .label{position:relative;text-align:center}
.service .label .dot{width:26px;height:26px;border-radius:50%;border:2px solid var(--white);margin:0 auto 6px}
.service .label h4{font-size:18px;font-weight:500;letter-spacing:.1em}
.service .label p{font-size:11px}

/* cta */
.cta{position:relative;height:300px;display:flex;flex-direction:column;align-items:center;justify-content:center;color:var(--white)}
.cta .ph{position:absolute;inset:0;background:linear-gradient(180deg,#9fb3c2 0%,#8ea4b4 45%,#b9ab98 100%)}
.cta .inner{position:relative;text-align:center}
.cta .msg{font-size:15px;letter-spacing:.08em;margin-bottom:24px}
.cta .row{display:flex;align-items:center;gap:50px}
.cta .tel{display:flex;align-items:center;gap:10px;font-family:"Montserrat",sans-serif;font-size:34px;font-weight:500}
.cta .tel small{font-size:11px;font-weight:700}
.cta .btn{border:1px solid var(--white);padding:12px 48px;font-size:13px}

/* footer */
.site-footer{display:flex;align-items:flex-start;padding:44px 100px 0 120px;gap:80px;height:320px}
.footer-brand .name{display:flex;align-items:center;gap:8px;font-family:"Montserrat",sans-serif;font-weight:700;font-size:19px;letter-spacing:.08em;color:var(--navy)}
.footer-brand .name i{width:16px;height:16px;border-radius:50%;background:var(--blue)}
.footer-brand p{font-size:11px;line-height:1.9;margin-top:10px}
.footer-links{display:grid;grid-template-columns:repeat(3,150px);align-content:start;gap:14px 30px;margin-left:auto;list-style:none;font-size:11px;line-height:1.6;padding-top:10px}
.footer-links li::before{content:"";display:inline-block;width:4px;height:4px;background:var(--blue);border-radius:50%;margin-right:8px;vertical-align:middle}
</style>
</head>
<body>

<section class="hero">
  <div class="ph" role="img" aria-label="砂浜の上を歩くフレンチブルドッグと海の写真" style="position:absolute;inset:0"></div>
  <div class="hero-copy">
    <p class="lead">Making a good living with your dog.</p>
    <p class="sub">フレンチブルドッグと暮らす毎日を。</p>
  </div>
</section>

<header class="site-header">
  <div class="brand"><span class="mark"></span><span class="name">PUPLEAF</span></div>
  <div class="header-info">
    <span>○○県○○市 フレンチブルドッグ専門ブリーダー｜大阪店</span>
    <span class="en">TEL 00-0000-0000</span>
    <span>営業 10:00-19:00</span>
  </div>
  <nav class="nav">
    <a href="#">店舗紹介<span>SHOP</span></a>
    <a href="#">ご購入の流れ<span>FLOW</span></a>
    <a href="#">子犬情報<span>PUPPY</span></a>
    <a href="#">よくある質問<span>FAQ</span></a>
    <a href="#">お客様の声<span>VOICE</span></a>
    <a href="#">お問い合わせ<span>CONTACT</span></a>
    <svg class="search" width="18" height="18" viewBox="0 0 18 18"><circle cx="7.5" cy="7.5" r="5.5" fill="none" stroke="#3a3a3a" stroke-width="1.6"/><line x1="11.5" y1="11.5" x2="16" y2="16" stroke="#3a3a3a" stroke-width="1.6"/></svg>
  </nav>
</header>

<section class="puppies">
  <div class="sec-title"><div class="dot"></div><h2>子犬情報</h2><p>PUPPY</p></div>
  <a class="more">More ▸</a>
  <div class="puppy-grid">
    <div class="puppy"><div class="ph" role="img" aria-label="芝生の上の子犬の写真" style="background:linear-gradient(160deg,#6ea35a,#a9c98a)"></div><p class="meta">2019.06.12 生 / 男の子</p><p class="price">¥300,000</p></div>
    <div class="puppy"><div class="ph" role="img" aria-label="クリーム色の子犬の写真" style="background:linear-gradient(160deg,#d8c6b3,#a48d78)"></div><p class="meta">2019.06.12 生 / 女の子</p><p class="price">¥280,000</p></div>
    <div class="puppy"><div class="ph" role="img" aria-label="室内の子犬の写真" style="background:linear-gradient(160deg,#e8e4df,#c9b9a7)"></div><p class="meta">2019.06.12 生 / 男の子</p><p class="price">¥300,000</p></div>
    <div class="puppy"><div class="ph" role="img" aria-label="ピンク背景の子犬の写真" style="background:linear-gradient(160deg,#f2b8c4,#e48da2)"></div><p class="meta">2019.06.12 生 / 女の子</p><p class="price">¥320,000</p></div>
    <div class="puppy"><div class="ph" role="img" aria-label="芝生の上の子犬の写真" style="background:linear-gradient(160deg,#7aa565,#c0d3a8)"></div><p class="meta">2019.06.12 生 / 男の子</p><p class="price">¥300,000</p></div>
    <div class="puppy"><div class="ph" role="img" aria-label="抱っこされた子犬の写真" style="background:linear-gradient(160deg,#d6d2cc,#8c8278)"></div><p class="meta">2019.06.12 生 / 女の子</p><p class="price">¥280,000</p></div>
    <div class="puppy"><div class="ph" role="img" aria-label="遊ぶ子犬の写真" style="background:linear-gradient(160deg,#e4ddd4,#b8a590)"></div><p class="meta">2019.06.12 生 / 男の子</p><p class="price">¥300,000</p></div>
    <div class="puppy"><div class="ph" role="img" aria-label="砂浜の子犬の写真" style="background:linear-gradient(160deg,#c9b697,#8f7b5e)"></div><p class="meta">2019.06.12 生 / 女の子</p><p class="price">¥320,000</p></div>
    <div class="puppy"><div class="ph" role="img" aria-label="黒い子犬の写真" style="background:linear-gradient(160deg,#b7bdb0,#4a4a45)"></div><p class="meta">2019.06.12 生 / 男の子</p><p class="price">¥300,000</p></div>
    <div class="puppy"><div class="ph" role="img" aria-label="並んだ子犬たちの写真" style="background:linear-gradient(160deg,#efe8e0,#c4b7a8)"></div><p class="meta">2019.06.12 生 / 女の子</p><p class="price">¥280,000</p></div>
  </div>
</section>

<section class="news">
  <div class="sec-title"><div class="dot"></div><h2>お知らせ</h2><p>NEWS</p></div>
  <a class="feed">▸ Feed on PupSnap</a>
  <div class="insta">
    <div class="ph" role="img" aria-label="犬の日常写真" style="background:linear-gradient(150deg,#cfc7be,#7d746a)"></div>
    <div class="ph" role="img" aria-label="子犬の寝姿の写真" style="background:linear-gradient(150deg,#e9ddd0,#c2a88f)"></div>
    <div class="ph" role="img" aria-label="子犬たちの写真" style="background:linear-gradient(150deg,#e6e1da,#a99886)"></div>
    <div class="ph" role="img" aria-label="芝生の犬の写真" style="background:linear-gradient(150deg,#7fa86a,#3f6a3a)"></div>
    <div class="ph" role="img" aria-label="公園の犬の写真" style="background:linear-gradient(150deg,#b5c9a2,#6b8c5c)"></div>
    <div class="ph" role="img" aria-label="室内の犬の写真" style="background:linear-gradient(150deg,#e3ddd6,#a5968a)"></div>
  </div>
</section>

<section class="about">
  <div class="about-photo ph" role="img" aria-label="ピンクのバギーに乗った三匹のフレンチブルドッグの写真"></div>
  <div class="about-card">
    <h3>フレンチブルドッグ専門だからこそ、<br>新しい出会いをお手伝いします。</h3>
    <p class="tag">Making a good living with your dog.</p>
    <p>○○ブリーダーは、フレンチブルドッグを専門に扱う小規模ブリーダーです。健康で性格の良い子犬を一頭ずつ丁寧に育て、安心してお迎えいただけるよう、ご購入後のサポートまで責任を持って対応しています。</p>
    <p>もちろん「ご見学だけでも大歓迎」です。実際に子犬と触れ合いながら、新しい家族との出会いをゆっくりとお楽しみください。</p>
  </div>
  <div class="shop">
    <div class="ph" role="img" aria-label="明るい店舗内観の写真"></div>
    <p class="name"><i></i>PUPLEAF</p>
    <p class="addr">〒000-0000 ○○県○○市○○町1-2-3<br>TEL 00-0000-0000（受付 10:00-19:00）<br>定休日 毎週水曜日</p>
    <p class="link">More information ▸</p>
  </div>
</section>

<section class="services">
  <a class="service">
    <span class="ph" role="img" aria-label="フレンチブルドッグの写真" style="background:linear-gradient(135deg,#3a3a3a,#6b6460 60%,#4a4542)"></span>
    <div class="label"><div class="dot"></div><h4>アフターサービス</h4><p>お迎え後も安心のサポート</p></div>
  </a>
  <a class="service">
    <span class="ph" role="img" aria-label="子犬を抱く人の写真" style="background:linear-gradient(135deg,#5a5450,#8a7f76 60%,#3f3a37)"></span>
    <div class="label"><div class="dot"></div><h4>ご購入の流れ</h4><p>お問い合わせからお迎えまで</p></div>
  </a>
</section>

<section class="cta">
  <div class="ph" role="img" aria-label="砂浜と海の写真"></div>
  <div class="inner">
    <p class="msg">ご購入まで不安な点がありましたら、お電話・フォームよりお気軽にご相談ください。</p>
    <div class="row">
      <div class="tel">
        <svg width="26" height="26" viewBox="0 0 24 24"><path d="M6.6 10.8a15 15 0 0 0 6.6 6.6l2.2-2.2c.3-.3.7-.4 1-.2 1.1.4 2.3.6 3.6.6.6 0 1 .4 1 1V20c0 .6-.4 1-1 1A17 17 0 0 1 3 4c0-.6.4-1 1-1h3.5c.6 0 1 .4 1 1 0 1.3.2 2.5.6 3.6.1.3 0 .7-.2 1z" fill="#fff"/></svg>
        <small>TEL</small>00-0000-0000
      </div>
      <a class="btn">お問い合わせフォーム ▸</a>
    </div>
  </div>
</section>

<footer class="site-footer">
  <div class="footer-brand">
    <p class="name"><i></i>PUPLEAF</p>
    <p>フレンチブルドッグ専門ブリーダー｜大阪店<br>〒000-0000 ○○県○○市○○町1-2-3<br>TEL 00-0000-0000</p>
  </div>
  <ul class="footer-links">
    <li>店舗紹介</li><li>子犬情報</li><li>お問い合わせ</li>
    <li>ご購入の流れ</li><li>アフターサービス</li><li>会社概要</li>
    <li>よくある質問</li><li>お知らせ</li><li>個人情報保護方針</li>
    <li>お客様の声</li><li>スタッフ紹介</li>
  </ul>
</footer>

</body>
</html>
```